RM Skyline Imaging Web Site design

I am looking for a responsive single page website deign for rmskylineimages.com. This is a drone based aerial photography and cinematography business. It should have an about us section, a services section that contains photograph service, Video footage, and Aerial mapping all under the services section, a pricing section, and then a contact page for customers to contact us.

Coding

Coded - Design and coding required

Number of Pages Required

1 page

Font styles to use
Sans Serif

Colors

Designer to choose colors to be used in the design.

Requirements
Must have
• Responsive design. About us section, services section, pricing section under the services links, and contact us section, that links to a submission page where they can send Name, address, email, and comments on what they are interested in.
• See hoverlens7.com - looking for similar design.
Should not have
• clutter, or too busy design

```html
<!DOCTYPE html>
<html lang="en">
<head>
<meta charset="utf-8">
<title>RM Skyline Imaging</title>
<link href="https://fonts.googleapis.com/css2?family=Raleway:wght@400;500;600;700&family=Open+Sans:wght@400;600;700&display=swap" rel="stylesheet">
<style>
:root{
  --orange:#f7941d;
  --ink:#222;
  --text:#555;
  --muted:#888;
  --line:#d9d9d9;
  --light:#f4f4f4;
  --dark:#2e2e2e;
  --player:#2a2a2a;
  --red:#c8151b;
}
*{box-sizing:border-box;margin:0;padding:0}
html,body{width:1200px;height:4891px;overflow:hidden;background:#fff}
body{position:relative;font-family:"Open Sans",Arial,sans-serif;color:var(--text)}
.abs{position:absolute}
/* header */
.site-header{left:0;top:0;width:1200px;height:82px;background:#fff;border-bottom:1px solid #eee}
.brand{display:flex;align-items:center;gap:10px;font-family:"Raleway",sans-serif;font-weight:600;letter-spacing:3px;font-size:17px;color:var(--ink)}
.brand .dot{width:14px;height:14px;border-radius:50%;background:var(--orange)}
.site-header .brand{position:absolute;left:160px;top:28px}
.nav{position:absolute;right:160px;top:30px;display:flex;gap:44px;font-family:"Raleway",sans-serif;font-weight:600;font-size:14px;color:var(--ink)}
.nav .active{color:var(--orange);border-bottom:2px solid var(--orange);padding-bottom:8px}
/* hero */
.hero{left:0;top:82px;width:1200px;height:505px;background:linear-gradient(160deg,#5f7b3e 0%,#8a8a78 40%,#a49f8e 55%,#4d6a2e 100%)}
.hero-copy{position:absolute;left:0;top:240px;width:1200px;text-align:center;color:#fff;font-family:"Raleway",sans-serif;font-weight:600;font-size:27px;line-height:36px;text-shadow:0 1px 4px rgba(0,0,0,.5)}
.btn-orange{display:inline-block;margin-top:12px;background:var(--orange);color:#222;font-size:19px;font-weight:700;padding:8px 22px;border-radius:4px;text-shadow:none}
/* headings */
.section-title{left:0;width:1200px;text-align:center;font-family:"Raleway",sans-serif;font-weight:500;font-size:33px;color:var(--ink)}
.section-title span{color:var(--orange)}
.section-title.light{color:#fff}
.rule{display:block;margin:10px auto 0;width:80px;height:3px;background:var(--orange);position:relative}
.rule:after{content:"";position:absolute;left:34px;top:-4px;width:11px;height:11px;border-radius:50%;background:var(--orange)}
.body-copy{font-size:12.5px;line-height:19px;color:var(--text);text-align:center}
/* video */
.video{background:var(--player);border-radius:8px;overflow:hidden}
.video .frame{position:absolute;left:0;top:0;right:0}
.video .bar{position:absolute;left:0;right:0;bottom:0;height:70px;background:linear-gradient(#3a3a3a,#1e1e1e)}
.play{position:absolute;width:110px;height:74px;border-radius:14px;background:rgba(20,20,20,.85);left:50%;top:50%;transform:translate(-50%,-50%)}
.play:after{content:"";position:absolute;left:44px;top:20px;border-left:28px solid #fff;border-top:17px solid transparent;border-bottom:17px solid transparent}
/* services */
.services{left:0;top:1532px;width:1200px;height:571px;background:linear-gradient(180deg,#2c3036 0%,#434850 50%,#2c3036 100%)}
.service{position:absolute;top:245px;width:280px;text-align:center;color:#fff}
.icon-ring{width:104px;height:104px;border-radius:50%;background:#fff;border:6px solid var(--orange);margin:0 auto;display:flex;align-items:center;justify-content:center}
.service h3{font-size:19px;font-weight:600;margin-top:24px}
.service p{font-size:12px;line-height:18px;color:#ddd;margin-top:20px}
/* thumbs */
.thumb{position:absolute;top:2902px;width:284px}
.thumb .pic{height:155px;position:relative;border-radius:3px;overflow:hidden}
.thumb .pic .mini{position:absolute;left:0;right:0;bottom:0;height:24px;background:#222}
.thumb .pic .mini i{position:absolute;left:60px;top:10px;width:90px;height:4px;background:var(--red)}
.thumb p{font-size:12px;line-height:17px;color:#444;margin-top:10px}
/* pricing */
.price-card{position:absolute;top:3315px;width:272px;height:271px;border:1px solid var(--line);text-align:center;padding-top:24px}
.price-card .icon-ring{width:74px;height:74px;border:2px solid var(--line)}
.price{color:var(--orange);font-size:40px;font-weight:400;margin-top:12px;font-family:"Raleway",sans-serif}
.price sup,.price sub{font-size:14px}
.price-card h3{font-size:17px;font-weight:700;color:var(--ink);margin-top:4px}
.price-card p{font-size:12px;line-height:18px;margin:14px 34px 0}
/* pilots */
.lead-photo{left:164px;top:3790px;width:228px;height:228px;border-radius:50%;border:7px solid var(--orange);background:linear-gradient(#7a8ea8,#33455e)}
.pilot{position:absolute;top:3982px;width:110px;text-align:center;font-size:10.5px;line-height:13px;color:#444}
.pilot .av{width:72px;height:72px;border-radius:50%;margin:0 auto 8px;background:linear-gradient(#9aa3ad,#3a4350)}
/* inquiry */
.inquiry{left:0;top:4189px;width:1200px;height:398px;background:var(--light)}
.field{position:absolute;height:36px;border:1px solid #cfcfcf;background:#fff;font-size:12px;color:#444;padding:10px 12px}
.field svg{position:absolute;right:10px;top:9px}
.submit{left:538px;top:4499px;width:101px;height:36px;background:#222;color:#fff;font-size:14px;font-weight:600;text-align:center;line-height:36px;letter-spacing:1px}
/* cta */
.cta{left:0;top:4587px;width:1200px;height:147px;background:var(--orange)}
.cta h2{position:absolute;left:188px;top:50px;font-family:"Raleway",sans-serif;font-weight:500;font-size:31px;color:#fff}
.cta .ask{position:absolute;left:890px;top:56px;width:112px;height:36px;background:#222;color:#fff;font-size:14px;font-weight:600;line-height:36px;text-align:center}
/* footer */
.site-footer{left:0;top:4734px;width:1200px;height:157px;background:var(--dark);color:#fff}
.site-footer .brand{position:absolute;left:0;width:1200px;justify-content:center;top:48px;color:#fff}
.site-footer small{position:absolute;left:0;width:1200px;top:112px;text-align:center;font-size:11px;color:#ccc}
</style>
</head>
<body>

<header class="abs site-header">
  <div class="brand"><span class="dot"></span>RM Skyline Imaging</div>
  <nav class="nav"><span class="active">Home</span><span>About Us</span><span>Services</span><span>Pricing</span><span>Contact Us</span></nav>
</header>

<section class="abs hero" role="img" aria-label="Aerial view of a stone manor house surrounded by trees with a drone in flight">
  <div class="hero-copy">We Are In A Drone Based<br>Aerial Photography And Cinematography Business<br><span class="btn-orange">Learn More</span></div>
</section>

<h2 class="abs section-title" style="top:622px">About <span>RM Skyline Imaging</span><i class="rule"></i></h2>
<p class="abs body-copy" style="left:172px;top:700px;width:856px">Lorem ipsum dolor sit amet, consectetuer adipiscing elit, sed diam nonummy nibh euismod tincidunt ut laoreet dolore magna aliquam erat volutpat. Ut wisi enim ad minim veniam, quis nostrud exerci tation ullamcorper suscipit lobortis nisl ut aliquip ex ea commodo consequat. Duis autem vel eum iriure dolor in hendrerit in vulputate velit esse molestie consequat, vel illum dolore eu feugiat nulla facilisis at vero eros et accumsan et iusto odio dignissim qui blandit praesent luptatum zzril delenit augue duis dolore te feugait nulla facilisi.</p>
<p class="abs body-copy" style="left:172px;top:790px;width:856px">Lorem ipsum dolor sit amet, consectetuer adipiscing elit, sed diam nonummy nibh euismod tincidunt ut laoreet dolore magna aliquam erat volutpat. Ut wisi enim ad minim veniam, quis nostrud exerci tation ullamcorper suscipit lobortis nisl ut aliquip ex ea commodo consequat. Duis autem vel eum iriure dolor in hendrerit in vulputate velit esse molestie consequat, vel illum dolore eu feugiat nulla facilisis at vero eros et accumsan et iusto odio dignissim qui blandit praesent luptatum zzril delenit augue duis dolore te feugait nulla facilisi.</p>

<div class="abs video" style="left:173px;top:897px;width:854px;height:570px">
  <div class="frame" style="bottom:70px;background:linear-gradient(180deg,#3f4f34 0%,#5d7041 45%,#6f8f3c 70%,#4f6b2a 100%)" role="img" aria-label="Couple in a park with trees, a drone hovering nearby"><span class="play"></span></div>
  <svg class="bar" width="854" height="70" viewBox="0 0 854 70"><rect width="854" height="70" fill="#262626"/><path d="M40 24 L40 48 L60 36Z" fill="#fff"/><path d="M104 30h8l10-8v28l-10-8h-8z" fill="#fff"/><path d="M128 28q6 8 0 16" stroke="#fff" stroke-width="2.5" fill="none"/><rect x="160" y="32" width="500" height="8" rx="4" fill="#555"/><rect x="160" y="32" width="215" height="8" rx="4" fill="var(--red)"/><path d="M800 24l8 0-8 8zM826 24l-8 0 8 8zM800 48l8 0-8-8zM826 48l-8 0 8-8z" fill="#fff"/></svg>
</div>

<section class="abs services" role="img" aria-label="Dusky aerial view of a city skyline">
  <h2 class="abs section-title light" style="top:58px">Our <span>Services</span><i class="rule"></i></h2>
  <div class="service" style="left:157px"><div class="icon-ring"><svg width="48" height="40" viewBox="0 0 48 40"><rect x="2" y="8" width="44" height="30" rx="5" fill="#222"/><rect x="16" y="2" width="16" height="8" rx="2" fill="#222"/><circle cx="24" cy="23" r="10" fill="#fff"/><circle cx="24" cy="23" r="6" fill="#222"/></svg></div><h3>Photograph Service</h3><p>Lorem ipsum dolor sit amet, consectetuer adipiscing elit, sed diam nonummy nibh euismod tincidunt ut laoreet dolore magna aliquam erat volutpat. Ut wisi enim ad minim veniam, quis nostrud exerci tation ullamcorper.</p></div>
  <div class="service" style="left:457px"><div class="icon-ring"><svg width="50" height="40" viewBox="0 0 50 40"><rect x="3" y="3" width="44" height="28" rx="3" fill="none" stroke="#222" stroke-width="4"/><path d="M20 10v14l12-7z" fill="#222"/><rect x="12" y="34" width="26" height="4" fill="#222"/></svg></div><h3>Video Footage</h3><p>Lorem ipsum dolor sit amet, consectetuer adipiscing elit, sed diam nonummy nibh euismod tincidunt ut laoreet dolore magna aliquam erat volutpat. Ut wisi enim ad minim veniam, quis nostrud exerci tation ullamcorper.</p></div>
  <div class="service" style="left:760px"><div class="icon-ring"><svg width="54" height="40" viewBox="0 0 54 40"><rect x="4" y="6" width="14" height="3" fill="#222"/><rect x="36" y="6" width="14" height="3" fill="#222"/><rect x="10" y="8" width="3" height="8" fill="#222"/><rect x="41" y="8" width="3" height="8" fill="#222"/><rect x="10" y="14" width="34" height="6" rx="3" fill="#222"/><rect x="19" y="18" width="16" height="12" rx="4" fill="#222"/><circle cx="27" cy="32" r="4" fill="#222"/></svg></div><h3>Aerial Mapping</h3><p>Lorem ipsum dolor sit amet, consectetuer adipiscing elit, sed diam nonummy nibh euismod tincidunt ut laoreet dolore magna aliquam erat volutpat. Ut wisi enim ad minim veniam, quis nostrud exerci tation ullamcorper.</p></div>
</section>

<h2 class="abs section-title" style="top:2135px">Recent <span>Work</span><i class="rule"></i></h2>
<div class="abs video" style="left:173px;top:2236px;width:854px;height:574px">
  <div class="frame" style="bottom:70px;background:linear-gradient(180deg,#8fa9c8 0%,#b9c6d2 30%,#a8a39a 55%,#5f7a3a 100%)" role="img" aria-label="Aerial view of a large suburban house with a drone flying above"><span class="play"></span></div>
  <svg class="bar" width="854" height="70" viewBox="0 0 854 70"><rect width="854" height="70" fill="#262626"/><path d="M40 24 L40 48 L60 36Z" fill="#fff"/><path d="M104 30h8l10-8v28l-10-8h-8z" fill="#fff"/><path d="M128 28q6 8 0 16" stroke="#fff" stroke-width="2.5" fill="none"/><rect x="160" y="32" width="500" height="8" rx="4" fill="#555"/><rect x="160" y="32" width="215" height="8" rx="4" fill="var(--red)"/><path d="M800 24l8 0-8 8zM826 24l-8 0 8 8zM800 48l8 0-8-8zM826 48l-8 0 8-8z" fill="#fff"/></svg>
</div>
<p class="abs" style="left:173px;top:2830px;width:854px;font-size:12px;line-height:17px;color:#444">Lorem ipsum dolor sit amet, consectetuer adipiscing elit, sed diam nonummy nibh euismod tincidunt ut laoreet dolore magna aliquam erat volutpat. Ut wisi enim ad minim veniam, quis nostrud exerci tation ullamcorper.</p>

<div class="thumb" style="left:163px"><div class="pic" style="background:linear-gradient(135deg,#d08a3a,#3b2a22)" role="img" aria-label="Drone flying at sunset"><span class="mini"><i></i></span></div><p>Lorem ipsum dolor sit amet, consectetuer adipiscing elit, sed diam nonummy nibh euismod.</p></div>
<div class="thumb" style="left:460px"><div class="pic" style="background:linear-gradient(135deg,#f2f2f2,#c9c9c9)" role="img" aria-label="Fixed wing mapping drone"><span class="mini"><i></i></span></div><p>Lorem ipsum dolor sit amet, consectetuer adipiscing elit, sed diam nonummy nibh euismod.</p></div>
<div class="thumb" style="left:753px"><div class="pic" style="background:linear-gradient(135deg,#a7b4c4,#5c5a55)" role="img" aria-label="Crowd gathered at an outdoor event"><span class="mini"><i></i></span></div><p>Lorem ipsum dolor sit amet, consectetuer adipiscing elit, sed diam nonummy nibh euismod.</p></div>

<h2 class="abs section-title" style="top:3222px">Our <span>Pricing</span><i class="rule"></i></h2>
<div class="price-card" style="left:163px"><div class="icon-ring"><svg width="34" height="28" viewBox="0 0 48 40"><rect x="2" y="8" width="44" height="30" rx="5" fill="#222"/><rect x="16" y="2" width="16" height="8" rx="2" fill="#222"/><circle cx="24" cy="23" r="10" fill="#fff"/><circle cx="24" cy="23" r="6" fill="#222"/></svg></div><div class="price"><sup>$</sup>200<sub>.00</sub></div><h3>Photograph Service</h3><p>Lorem ipsum dolor sit amet, consectetuer adipiscing elit, sed diam nonummy nibh euismod tincidunt ut.</p></div>
<div class="price-card" style="left:450px"><div class="icon-ring"><svg width="34" height="28" viewBox="0 0 50 40"><rect x="3" y="3" width="44" height="28" rx="3" fill="none" stroke="#222" stroke-width="4"/><path d="M20 10v14l12-7z" fill="#222"/><rect x="12" y="34" width="26" height="4" fill="#222"/></svg></div><div class="price"><sup>$</sup>200<sub>.00</sub></div><h3>Video Footage</h3><p>Lorem ipsum dolor sit amet, consectetuer adipiscing elit, sed diam nonummy nibh euismod tincidunt ut.</p></div>
<div class="price-card" style="left:747px"><div class="icon-ring"><svg width="38" height="28" viewBox="0 0 54 40"><rect x="4" y="6" width="14" height="3" fill="#222"/><rect x="36" y="6" width="14" height="3" fill="#222"/><rect x="10" y="8" width="3" height="8" fill="#222"/><rect x="41" y="8" width="3" height="8" fill="#222"/><rect x="10" y="14" width="34" height="6" rx="3" fill="#222"/><rect x="19" y="18" width="16" height="12" rx="4" fill="#222"/><circle cx="27" cy="32" r="4" fill="#222"/></svg></div><div class="price"><sup>$</sup>200<sub>.00</sub></div><h3>Aerial Mapping</h3><p>Lorem ipsum dolor sit amet, consectetuer adipiscing elit, sed diam nonummy nibh euismod tincidunt ut.</p></div>

<h2 class="abs section-title" style="top:3700px">Our <span>Drone Pilots</span><i class="rule"></i></h2>
<div class="abs lead-photo" role="img" aria-label="Portrait of the owner and lead pilot"></div>
<div class="abs" style="left:430px;top:3742px;font-size:17px;font-weight:600;color:var(--ink)">Owen Marlow <span style="font-size:11px;font-weight:400;color:var(--muted)">Owner / Pilot</span></div>
<p class="abs" style="left:430px;top:3776px;width:610px;font-size:12px;line-height:18px;color:#444">Lorem ipsum dolor sit amet, consectetuer adipiscing elit, sed diam nonummy nibh euismod tincidunt ut laoreet dolore magna aliquam erat volutpat. Ut wisi enim ad minim veniam, quis nostrud exerci tation ullamcorper suscipit lobortis nisl ut aliquip ex ea commodo consequat. Duis autem vel eum iriure dolor in hendrerit in vulputate velit esse molestie consequat, vel illum dolore eu feugiat nulla facilisis at vero eros et accumsan et iusto odio dignissim qui blandit praesent luptatum zzril delenit augue duis dolore te feugait nulla facilisi.</p>
<div class="pilot" style="left:330px"><div class="av" role="img" aria-label="Pilot portrait"></div>Owen Marlow<br>Owner / Pilot</div>
<div class="pilot" style="left:444px"><div class="av" role="img" aria-label="Pilot portrait"></div>Tobin Reyes</div>
<div class="pilot" style="left:565px"><div class="av" role="img" aria-label="Pilot portrait"></div>Felix Amato</div>
<div class="pilot" style="left:688px"><div class="av" role="img" aria-label="Pilot portrait"></div>Grant Delaney</div>
<div class="pilot" style="left:809px"><div class="av" role="img" aria-label="Pilot portrait"></div>Iris Navarro<br>CPA/CA</div>

<section class="abs inquiry">
  <h2 class="abs section-title" style="top:55px">Quick <span>Inquiry</span><i class="rule"></i></h2>
</section>
<div class="field" style="left:215px;top:4336px;width:378px">Name<svg width="16" height="16" viewBox="0 0 16 16"><circle cx="8" cy="5" r="3.5" fill="none" stroke="#666" stroke-width="1.4"/><path d="M2 15c0-4 12-4 12 0" fill="none" stroke="#666" stroke-width="1.4"/></svg></div>
<div class="field" style="left:215px;top:4388px;width:378px">Company<svg width="16" height="16" viewBox="0 0 16 16"><rect x="4" y="2" width="8" height="13" fill="none" stroke="#666" stroke-width="1.4"/><rect x="6" y="5" width="4" height="2" fill="#666"/></svg></div>
<div class="field" style="left:215px;top:4440px;width:378px">Email<svg width="16" height="16" viewBox="0 0 16 16"><rect x="1.5" y="3.5" width="13" height="9" fill="none" stroke="#666" stroke-width="1.4"/><path d="M2 4l6 5 6-5" fill="none" stroke="#666" stroke-width="1.4"/></svg></div>
<div class="field" style="left:610px;top:4336px;width:368px">Inquiry For<svg width="16" height="16" viewBox="0 0 16 16"><path d="M3 13l9-9 2 2-9 9H3z" fill="none" stroke="#666" stroke-width="1.4"/></svg></div>
<div class="field" style="left:610px;top:4388px;width:368px;height:88px">Message<svg width="16" height="16" viewBox="0 0 16 16"><path d="M3 13l9-9 2 2-9 9H3z" fill="#666"/></svg></div>
<div class="abs submit">SUBMIT</div>

<section class="abs cta">
  <h2>Have questions about drone services?</h2>
  <span class="ask">ASK NOW</span>
</section>

<footer class="abs site-footer">
  <div class="brand"><span class="dot"></span>RM Skyline Imaging</div>
  <small>Copyright © 2017, RM Skyline Imaging . All Rights Reserved</small>
</footer>

</body>
</html>
```